New Business Card Design Project

Make a kick ass business card for The Otter Tea Mug, using the designs. I also might like the 2nd place design logo on the back? Maybe all black with that? Not sure. Also, I'm cool with it being on metal, plastic, glass? or whatever for the business card. Maybe shaped like a shark? Let me know what else you need? Would like designs in the next day or so. Thank you.
Target Market(s)
Anyone that is cool
Contact Information for Business Card
Name: Dorian Fenwick
Phone: 317.594.8126
inventor/creator/entrepreneur/owner
www.theottertyeamug.example
social media links
https://www.facebook.com/theottertyeamug
https://twitter.com/otter_brew
https://www.instagram.com/theottertyeamug/
I'll get the Pinterest one soon
Colors
Designer to choose colors to be used in the design.
Requirements
Must have
- The Otter Tea Mug
- www.theottertyeamug.example
- social media tags?
- My logos and picture/photo of wine glass
Nice to have
- Maybe shaped like a wine glass or shark
- I'll let you decide but my same colors from my website would be nice

```html
<!DOCTYPE html>
<html lang="en">
<head>
<meta charset="utf-8">
<title>Otter Tea Mug — Business Card</title>
<link rel="stylesheet" href="https://fonts.googleapis.com/css2?family=Open+Sans:wght@400;700&display=swap">
<style>
  :root {
    --page: #e9e6e1;
    --card: #f3f3f4;
    --ink: #4a4a4a;
    --muted: #5c5c5c;
    --wordmark: #7a7a7a;
    --accent: #b8323a;
    --decor-light: #dcdcdd;
    --decor-mid: #cfcfd1;
    --icon: #3f4a5a;
    --shark-a: #8e1d3d;
    --shark-b: #c9303e;
    --shark-c: #a14a6e;
  }
  * { box-sizing: border-box; margin: 0; padding: 0; }
  html, body { width: 900px; height: 1200px; overflow: hidden; }
  body {
    background: var(--page);
    font-family: "Open Sans", Arial, sans-serif;
    position: relative;
  }
  .card {
    position: absolute;
    left: 77px;
    width: 746px;
    height: 436px;
    background: var(--card);
    box-shadow: 0 3px 8px rgba(0,0,0,0.18);
  }
  .card--front { top: 134px; }
  .card--back { top: 639px; }

  .shark-mark {
    position: absolute;
    left: 236px; top: 134px;
    width: 258px; height: 97px;
    border-radius: 50% 40% 45% 50% / 60% 50% 50% 40%;
    background: radial-gradient(ellipse at 55% 55%, var(--shark-b), var(--shark-a) 55%, var(--shark-c) 75%, transparent 100%);
    opacity: 0.85;
  }
  .wordmark {
    position: absolute;
    left: 143px; top: 254px;
    font-size: 54px;
    font-weight: 400;
    color: var(--wordmark);
    letter-spacing: 0.5px;
    line-height: 1;
    white-space: nowrap;
  }
  .glass-decor {
    position: absolute;
    border-radius: 45% 45% 12% 12% / 40% 40% 8% 8%;
    background: linear-gradient(180deg, var(--decor-mid), var(--decor-light) 60%, var(--card));
  }
  .glass-decor--front { left: 580px; top: 78px; width: 119px; height: 270px; }
  .glass-decor--back { left: 133px; top: 126px; width: 85px; height: 198px; }

  .divider {
    position: absolute;
    left: 346px; top: 125px;
    width: 1.5px; height: 188px;
    background: linear-gradient(180deg, transparent, var(--accent) 15%, var(--accent) 85%, transparent);
  }
  .identity {
    position: absolute;
    left: 401px; top: 122px;
  }
  .identity__name {
    font-size: 26px;
    color: var(--ink);
    font-weight: 400;
    line-height: 1.2;
    text-transform: uppercase;
  }
  .identity__first { color: var(--accent); font-weight: 700; }
  .identity__role {
    font-size: 16px;
    color: var(--muted);
    margin-top: 2px;
  }
  .contacts {
    position: absolute;
    left: 397px; top: 209px;
    list-style: none;
  }
  .contacts__item {
    display: flex;
    align-items: center;
    height: 25.7px;
    font-size: 17.5px;
    color: var(--ink);
    white-space: nowrap;
  }
  .contacts__icon {
    width: 19px; height: 19px;
    border-radius: 50%;
    background: var(--icon);
    margin-right: 18px;
    flex: none;
    display: flex; align-items: center; justify-content: center;
  }
</style>
</head>
<body>
  <section class="card card--front" aria-label="Card front">
    <div class="shark-mark" role="img" aria-label="Brand illustration made of red and purple dots"></div>
    <div class="wordmark">OtterTeaMug</div>
    <div class="glass-decor glass-decor--front" role="img" aria-label="Faint illustration of a glass with the brand emblem inside"></div>
  </section>

  <section class="card card--back" aria-label="Card back">
    <div class="glass-decor glass-decor--back" role="img" aria-label="Faint illustration of a glass with the brand emblem inside"></div>
    <div class="divider"></div>
    <div class="identity">
      <p class="identity__name"><span class="identity__first">Dorian</span> Fenwick</p>
      <p class="identity__role">owner</p>
    </div>
    <ul class="contacts">
      <li class="contacts__item">
        <span class="contacts__icon">
          <svg width="11" height="11" viewBox="0 0 24 24" aria-hidden="true"><path fill="#fff" d="M6.6 10.8a15.1 15.1 0 0 0 6.6 6.6l2.2-2.2c.3-.3.7-.4 1-.2 1.1.4 2.3.6 3.6.6.6 0 1 .4 1 1V20c0 .6-.4 1-1 1C10.6 21 3 13.4 3 4c0-.6.4-1 1-1h3.5c.6 0 1 .4 1 1 0 1.3.2 2.5.6 3.6.1.3 0 .7-.2 1z"/></svg>
        </span>317.594.8126
      </li>
      <li class="contacts__item"><span class="contacts__icon"></span>facebook.com/theottertyeamug</li>
      <li class="contacts__item"><span class="contacts__icon"></span>instagram.com/theottertyeamug</li>
      <li class="contacts__item"><span class="contacts__icon"></span>twitter.com/otter_brew</li>
    </ul>
  </section>
</body>
</html>
```